New solo practice law firm is looking for an elegant, professional, and interactive web design

I need a web design and developer for a new small law firm in Sacramento, California called Dorian Kessel Law, A Professional Corporation. I am a trial lawyer who represents average people facing difficult litigation disputes, including criminal defense as a former prosecutor and civil litigation as a civil litigator. Criminal defense includes domestic violence, battery, assault, drug possession, theft, DUI, etc. Civil litigation includes business disputes, property disputes, employment disputes, family law disputes, and immigration issues. I would like to see web designs that incorporate my logo and use the logo's navy blue and gold colors. I have uploaded the files of my logo to this brief. Please only use the navy blue and gold version. Overall, I want the design to look firm, professional, and elegant.

I plan on having the following pages on my website: (1) Home, (2) Dorian Kessel, (3) Practice Areas, (4) Insights, (5) Contact. I've hand drawn a preliminary sketch concept of what I envision the home page's layout to look like (attached with a text version). I would like your design to keep a similar layout for the homepage and incorporate my logo's colors within it but I am open to creative layout alternatives/ideas. I would like the other pages to have a similar look and feel as the home page. Some of the areas currently in my sketch do not have the full text. You can insert other text for now and I will provide the winner the full text.

In terms of the pictures on the website, I enjoy images of courthouses, columns (example attached but I cannot use this one), and, if possible, images from Sacramento, CA in my background (headshot attached). A plus would be live images that move and also sections of the webpage moving in the viewers view as they scroll down on the page. Also, it would be great to have my logo act as the tab for the website. I can provide other versions of the logo if needed.

I look forward to seeing your Wordpress designs!

People needing legal representation.

Law

Coded - Design and coding required

5+ page

Serif

• Incorporate my logo and my logo's colors.
• Live pictures and images appearing as viewers scroll on page.

```html
<!DOCTYPE html>
<html lang="en">
<head>
<meta charset="utf-8">
<title>Dorian Kessel Law</title>
<link href="https://fonts.googleapis.com/css2?family=Montserrat:wght@400;500;600&family=Arimo:ital,wght@0,400;0,700;1,400&display=swap" rel="stylesheet">
<style>
:root{
  --navy:#14213a;
  --navy-2:#1b2a47;
  --gold:#a88f5a;
  --gold-light:#c2ab78;
  --gold-deep:#8f7745;
  --ink:#1c2740;
  --body:#5b5f68;
  --paper:#ffffff;
  --mist:#eef0f2;
}
*{margin:0;padding:0;box-sizing:border-box}
html,body{width:1200px;height:3424px;overflow:hidden}
body{position:relative;background:var(--paper);font-family:"Arimo",Arial,sans-serif;color:var(--body)}
.abs{position:absolute}
.head{font-family:"Montserrat",Arial,sans-serif;font-weight:500;letter-spacing:1px;text-transform:uppercase}
.gold{color:var(--gold)}
.btn{position:absolute;border:1px solid var(--gold);outline:1px solid var(--gold);outline-offset:3px;
  font-family:"Arimo",Arial,sans-serif;font-weight:700;font-size:14px;color:var(--gold);
  display:flex;align-items:center;justify-content:center;letter-spacing:.5px}
.diamond{position:absolute;width:36px;height:36px;left:582px;transform:rotate(45deg);background:var(--gold);
  box-shadow:0 0 0 3px #fff,0 0 0 4px var(--gold)}
.diamond::after{content:"";position:absolute;left:11px;top:11px;width:9px;height:9px;border-right:1.5px solid #fff;border-bottom:1.5px solid #fff}

/* header */
.brand-box{left:0;top:0;width:217px;height:116px;background:#fff;display:flex;flex-direction:column;align-items:center;justify-content:center;z-index:3}
.brand-name{font-family:"Montserrat",Arial,sans-serif;font-weight:500;color:var(--gold);font-size:11px;letter-spacing:1.5px;text-align:center;line-height:1.5}
.brand-mark{width:30px;height:30px;border:1.5px solid var(--gold);margin-bottom:8px}
.topinfo{top:18px;display:flex;align-items:center;gap:12px;font-size:12px;color:var(--ink);line-height:1.6}
.icon-c{width:38px;height:38px;border-radius:50%;background:var(--navy);display:flex;align-items:center;justify-content:center}
.lang{left:1050px;top:20px;width:89px;height:32px;border:1px solid #9a9a9a;font-size:12px;color:var(--ink);display:flex;align-items:center;padding-left:14px}
.nav{left:217px;top:76px;width:923px;height:40px;border-radius:0 20px 20px 0;background:linear-gradient(90deg,var(--gold-deep),var(--gold-light) 60%,var(--gold));display:flex;align-items:center;z-index:3}
.nav a{color:#fff;font-size:11px;text-decoration:none;letter-spacing:.5px;text-align:center;border-right:1px solid rgba(255,255,255,.35);line-height:14px}
.nav a:last-child{border:none}

/* hero */
.hero-title{left:106px;top:240px;font-family:"Montserrat",Arial,sans-serif;font-weight:600;font-size:44px;line-height:48px;color:#fff}
.hero-sub{left:108px;top:404px;font-family:"Montserrat",Arial,sans-serif;font-size:13px;line-height:20px;color:#fff}
.arrow-btn{top:346px;width:37px;height:37px;background:rgba(255,255,255,.15);display:flex;align-items:center;justify-content:center}

/* intro */
.center{left:0;width:1200px;text-align:center}
.rule{position:absolute;height:1px;background:var(--gold)}
.intro-p{left:360px;top:908px;width:480px;text-align:center;font-size:12px;line-height:21px}

/* cards */
.card{position:absolute;top:1357px;width:241px;height:284px}
.card-label{position:absolute;left:0;bottom:0;width:100%;height:55px;background:var(--navy);color:#fff;
  font-family:"Montserrat",Arial,sans-serif;font-weight:500;font-size:18px;display:flex;align-items:center;justify-content:center;letter-spacing:.3px}
.card.active .card-label{background:var(--gold)}

/* ready */
.ready-p{left:169px;width:352px;font-size:12px;line-height:19.5px}

/* form */
.field{position:absolute;background:#fff;font-size:11px;color:#555;padding:14px 15px}

/* footer */
.f-head{font-family:"Montserrat",Arial,sans-serif;font-weight:500;font-size:14px;color:var(--gold);letter-spacing:.5px}
.f-text{font-size:12px;color:#fff;line-height:20px}
.links{list-style:none}
.links li{font-size:12px;color:#fff;height:22.6px;position:relative;padding-left:20px}
.links li::before{content:"";position:absolute;left:0;top:5px;width:5px;height:5px;background:var(--gold)}
.ring{width:37px;height:37px;border-radius:50%;border:1px solid var(--gold)}
</style>
</head>
<body>

<!-- HERO BACKGROUND -->
<svg class="abs" style="left:0;top:0" width="1200" height="720" viewBox="0 0 1200 720" aria-hidden="true">
  <defs>
    <linearGradient id="heroSky" x1="0" y1="0" x2="1" y2="1">
      <stop offset="0" stop-color="#1c2638"/>
      <stop offset=".5" stop-color="#3a4558"/>
      <stop offset="1" stop-color="#566175"/>
    </linearGradient>
    <linearGradient id="suit" x1="0" y1="0" x2="0" y2="1">
      <stop offset="0" stop-color="#8a6a55"/>
      <stop offset=".25" stop-color="#2b2b2e"/>
      <stop offset="1" stop-color="#121316"/>
    </linearGradient>
    <clipPath id="heroClip"><polygon points="0,0 1200,0 1200,605 600,698 0,605"/></clipPath>
  </defs>
  <g clip-path="url(#heroClip)">
    <rect width="1200" height="720" fill="url(#heroSky)" role="img" aria-label="Courthouse columns under a cloudy sky"/>
    <polygon points="935,250 1140,400 935,550 730,400" fill="none" stroke="var(--gold)" stroke-width="8" opacity=".75"/>
    <rect x="790" y="173" width="307" height="500" rx="120" fill="url(#suit)" role="img" aria-label="Portrait of the attorney in a dark suit"/>
  </g>
  <polygon points="550,700 600,649 650,700 650,724 550,724" fill="#fff" stroke="var(--gold)" stroke-width="1.5"/>
  <rect x="588" y="680" width="24" height="24" fill="none" stroke="var(--gold)" stroke-width="1.5"/>
</svg>

<!-- HEADER -->
<div class="abs brand-box">
  <div class="brand-mark"></div>
  <div class="brand-name">DORIAN KESSEL LAW<br>A PROFESSIONAL CORPORATION</div>
</div>
<div class="abs topinfo" style="left:532px">
  <div class="icon-c"><svg width="16" height="18" viewBox="0 0 16 18"><path d="M8 1a6 6 0 0 0-6 6c0 4.5 6 10 6 10s6-5.5 6-10a6 6 0 0 0-6-6z" fill="none" stroke="var(--gold)" stroke-width="1.5"/><circle cx="8" cy="7" r="2" fill="var(--gold)"/></svg></div>
  <div>4720 Larkspur Ave Suite<br># 210 Elk Grove, CA 95758</div>
</div>
<div class="abs topinfo" style="left:804px">
  <div class="icon-c"><svg width="18" height="18" viewBox="0 0 18 18"><path d="M4 2l3 3-2 2c1 2 3 4 5 5l2-2 3 3-2 3C8 16 2 10 2 4z" fill="none" stroke="var(--gold)" stroke-width="1.5"/></svg></div>
  <div><span style="color:var(--gold);font-size:11px">Free Consultation</span><br><span style="font-family:Montserrat,Arial,sans-serif;font-weight:600;font-size:19px;color:var(--ink)">(916)555-0142</span></div>
</div>
<div class="abs lang">English
  <svg class="abs" style="left:68px;top:12px" width="10" height="7" viewBox="0 0 10 7"><path d="M1 1l4 4 4-4" fill="none" stroke="#555" stroke-width="1.3"/></svg>
</div>
<nav class="abs nav">
  <a style="width:160px;padding-left:20px">HOME</a>
  <a style="width:190px">DORIAN KESSEL</a>
  <a style="width:188px">PRACTICE AREAS</a>
  <a style="width:140px">INSIGHTS</a>
  <a style="width:165px">CONTACT</a>
</nav>

<!-- HERO TEXT -->
<h1 class="abs hero-title"><span class="gold">Dorian Kessel</span><br>Professional<br>Corporation Law</h1>
<p class="abs hero-sub">I Am A Trial Lawyer Who Represents Average People Facing<br>Difficult Litigation Disputes</p>
<div class="btn" style="left:110px;top:461px;width:136px;height:38px;font-family:Montserrat,Arial,sans-serif;font-weight:600;color:var(--gold);outline-color:var(--gold)">CONTACT US</div>
<div class="abs arrow-btn" style="left:41px"><svg width="10" height="16"><path d="M8 1L2 8l6 7" fill="none" stroke="#fff" stroke-width="1.3"/></svg></div>
<div class="abs arrow-btn" style="left:1122px"><svg width="10" height="16"><path d="M2 1l6 7-6 7" fill="none" stroke="#fff" stroke-width="1.3"/></svg></div>

<!-- INTRO -->
<h2 class="abs center head" style="top:794px;font-size:31px;line-height:37px;color:var(--ink)">Criminal and Civil<br><span class="gold">Trial Lawyers</span></h2>
<div class="rule" style="left:490px;top:880px;width:220px"></div>
<p class="abs intro-p">Dorian Kessel Law is a law firm serving the Sacramento, Yolo, San Joaquin, Solano and Stanislaus Counties. We represent clients in a wide array of criminal, civil, family law, and immigration cases.</p>
<div class="btn" style="left:532px;top:996px;width:134px;height:36px">LEARN MORE</div>

<!-- PRACTICE AREAS -->
<svg class="abs" style="left:0;top:1130px" width="1200" height="750" viewBox="0 1130 1200 750" aria-hidden="true">
  <defs>
    <linearGradient id="mist" x1="0" y1="0" x2="1" y2="1">
      <stop offset="0" stop-color="#e4e7ea"/><stop offset=".5" stop-color="#f1f2f3"/><stop offset="1" stop-color="#dfe2e5"/>
    </linearGradient>
  </defs>
  <polygon points="0,1223 600,1136 1200,1223 1200,1781 600,1874 0,1781" fill="url(#mist)" role="img" aria-label="Faded background of legal documents on a desk"/>
</svg>
<div class="diamond" style="top:1113px"></div>
<h2 class="abs center head" style="top:1220px;font-size:29px;line-height:34px;color:var(--ink)">Our Practice<br><span class="gold">Areas</span></h2>
<div class="rule" style="left:562px;top:1304px;width:76px"></div>

<div class="card" style="left:85px">
  <svg width="241" height="229" role="img" aria-label="Photo of handcuffed hands"><polygon points="0,30 120,0 241,30 241,229 0,229" fill="#6e5a4c"/></svg>
  <div class="card-label">Criminal Defense</div>
</div>
<div class="card" style="left:348px">
  <svg width="241" height="229" role="img" aria-label="Photo of a gavel on banknotes"><polygon points="0,30 120,0 241,30 241,229 0,229" fill="#7b705f"/></svg>
  <div class="card-label">Civil Litigation</div>
</div>
<div class="card active" style="left:611px">
  <svg width="241" height="229" role="img" aria-label="Photo of a passport"><polygon points="0,30 120,0 241,30 241,229 0,229" fill="#2c3347"/></svg>
  <div class="card-label">Immigration</div>
</div>
<div class="card" style="left:873px">
  <svg width="241" height="229" role="img" aria-label="Photo of family figures beside a gavel"><polygon points="0,30 120,0 241,30 241,229 0,229" fill="#8d9398"/></svg>
  <div class="card-label">Family Law</div>
</div>

<p class="abs center" style="top:1710px;font-family:Montserrat,Arial,sans-serif;font-weight:500;font-size:18px;color:var(--ink)">Need An Help? Get Free Consultation On</p>
<div class="btn" style="left:472px;top:1751px;width:256px;height:42px;font-family:Montserrat,Arial,sans-serif;font-weight:600;font-size:26px">(916)555-0142</div>
<div class="diamond" style="top:1861px"></div>

<!-- CONSULTATION BAND + FOOTER BG -->
<svg class="abs" style="left:0;top:2380px" width="1200" height="1044" viewBox="0 2380 1200 1044" aria-hidden="true">
  <defs>
    <linearGradient id="goldBand" x1="0" y1="0" x2="1" y2="0">
      <stop offset="0" stop-color="#8f7a4c"/><stop offset=".5" stop-color="#b39c6b"/><stop offset="1" stop-color="#9c8655"/>
    </linearGradient>
  </defs>
  <rect x="0" y="2880" width="1200" height="544" fill="var(--navy)"/>
  <polygon points="0,2505 600,2403 1200,2480 1200,2891 600,2983 0,2891" fill="url(#goldBand)" role="img" aria-label="Gold toned courthouse facade"/>
</svg>

<!-- READY -->
<h2 class="abs head" style="left:169px;top:1982px;font-size:29px;line-height:38px;color:var(--ink)">Ready, Reliable, &amp;<br><span class="gold">Experienced</span></h2>
<div class="rule" style="left:169px;top:2068px;width:70px"></div>
<p class="abs ready-p" style="top:2092px">Lorem Ipsum has been the industry's standard dummy text ever since the 1500s, when an unknown printer took a galley of type and scrambled it to make a type specimen book.</p>
<p class="abs ready-p" style="top:2160px">Lorem Ipsum has been the industry's standard dummy text ever since the 1500s, when an unknown printer took a galley of type and scrambled it to make a type specimen book. It has survived not only five centuries, but also the leap into electronic industry typesetting, remaining essentially unchanged.</p>
<div class="btn" style="left:173px;top:2285px;width:151px;height:38px">ABOUT DORIAN</div>
<svg class="abs" style="left:751px;top:1964px" width="300" height="512" role="img" aria-label="Portrait of the attorney in a dark suit">
  <defs><linearGradient id="suit2" x1="0" y1="0" x2="0" y2="1"><stop offset="0" stop-color="#8a6a55"/><stop offset=".28" stop-color="#2b2b2e"/><stop offset="1" stop-color="#121316"/></linearGradient></defs>
  <rect width="300" height="512" rx="110" fill="url(#suit2)"/>
</svg>
<div class="diamond" style="top:2386px"></div>

<!-- FORM -->
<h2 class="abs center head" style="top:2514px;font-size:30px;line-height:37px;color:var(--navy)">Schedule a Free<br><span style="color:#fff">Consultation</span></h2>
<div class="rule" style="left:565px;top:2602px;width:70px;background:#fff"></div>
<p class="abs center" style="top:2623px;font-size:13px;font-style:italic;color:#fff">When You Contact Dorian Kessel Law For a Free Consultation...</p>
<div class="field" style="left:206px;top:2671px;width:255px;height:42px">Name *</div>
<div class="field" style="left:472px;top:2671px;width:255px;height:42px">Email *</div>
<div class="field" style="left:739px;top:2671px;width:255px;height:42px">Phone Number*</div>
<div class="field" style="left:206px;top:2726px;width:788px;height:90px">Please Enter a Brief Description of Your Case</div>
<div class="btn" style="left:534px;top:2833px;width:132px;height:38px;color:#fff;border-color:#fff;outline-color:#fff">SUBMIT</div>
<div class="diamond" style="top:2968px"></div>

<!-- FOOTER -->
<div class="abs" style="left:80px;top:3080px;width:200px;text-align:center">
  <div style="width:44px;height:44px;border:1.5px solid var(--gold);margin:0 auto 18px"></div>
  <div class="brand-name" style="font-size:13px;letter-spacing:2px">DORIAN KESSEL LAW<br>A PROFESSIONAL CORPORATION</div>
</div>

<div class="abs f-head" style="left:338px;top:3062px">CONTACT INFO</div>
<div class="abs" style="left:335px;top:3103px;display:flex;gap:16px;align-items:center">
  <div class="ring" style="display:flex;align-items:center;justify-content:center"><svg width="14" height="17" viewBox="0 0 16 18"><path d="M8 1a6 6 0 0 0-6 6c0 4.5 6 10 6 10s6-5.5 6-10a6 6 0 0 0-6-6z" fill="none" stroke="var(--gold)" stroke-width="1.5"/><circle cx="8" cy="7" r="2" fill="var(--gold)"/></svg></div>
  <div class="f-text">4720 Larkspur Ave Suite #<br>210 Elk Grove, CA 95758</div>
</div>
<div class="abs" style="left:335px;top:3158px;display:flex;gap:16px;align-items:center">
  <div class="ring" style="display:flex;align-items:center;justify-content:center"><svg width="16" height="16" viewBox="0 0 18 18"><path d="M4 2l3 3-2 2c1 2 3 4 5 5l2-2 3 3-2 3C8 16 2 10 2 4z" fill="none" stroke="var(--gold)" stroke-width="1.5"/></svg></div>
  <div class="f-text" style="font-size:16px">(916) 555-0142</div>
</div>

<div class="abs f-head" style="left:613px;top:3062px">QUICK LINKS</div>
<ul class="abs links" style="left:612px;top:3102px">
  <li>Home</li><li>Dorian Kessel</li><li>Practice Areas</li><li>Insights</li><li>Contact</li><li>Privacy Policy</li>
</ul>

<div class="abs f-head" style="left:888px;top:3062px">FOLLOW US</div>
<div class="abs" style="left:887px;top:3101px;display:flex;gap:8px">
  <div class="ring" role="img" aria-label="Social profile one"></div>
  <div class="ring" role="img" aria-label="Social profile two"></div>
  <div class="ring" role="img" aria-label="Social profile three"></div>
</div>

<div class="rule" style="left:61px;top:3277px;width:1078px;background:rgba(255,255,255,.12)"></div>
<p class="abs" style="left:61px;top:3312px;width:1060px;font-size:11px;line-height:20px;color:#9aa3b5">The information on this website is for general information purposes only. Nothing on this site should be taken as legal advice for any individual case or situation. This information is not intended to create, and receipt of viewing does not constitute an attorney-client relationship</p>
<p class="abs" style="left:61px;top:3366px;font-size:11px;color:#fff"><span class="gold">©Dorian Kessel Law A Professional Corporation</span> - 2021 All Rights Reserved</p>

</body>
</html>
```